Creative Landscape Architecture Company Needs a Creative Business Card Design

Marsh and Partners, Inc. is a landscape architecture (LA) company started in 1997 in Austin, TX. We work on large commerical projects all around the U.S. and provide land planning, site planning, landscape design and architectural renderings.

We don't want this card to look like a LA firm's business card. We are looking for a business card design that is edgy and cool to reflect the more artistic and creative side of our company. We would like our clients to think "now there's a business card unlike any other LA that I've seen before."

We would like it to be in standard 2"x3.5" format. Double sided. Full color ok. Our company logo is attached. We like the logo but would not be adverse to any variations you would like to make to it. Feel free to change it up. Typically the logo has been a light saturated orange color but its not necessary that you stick with it.

Requirements
Must have
• 1. Company name
2. individuals name
3. email address
4. cell number
5. office number
6. website: www.marshandpartners-demo.net
7. Business address
Nice to have
• Can add (but not necessary)
Personal titles such as "president" or "registered landscape architect"

```html
<!DOCTYPE html>
<html lang="en">
<head>
<meta charset="utf-8">
<title>Marsh and Partners – Business Card</title>
<link href="https://fonts.googleapis.com/css2?family=Didact+Gothic&display=swap" rel="stylesheet">
<style>
  :root {
    --card-bg: #e2f3b0;
    --leaf-dark: #3ba23f;
    --leaf-mid: #8cc63f;
    --leaf-yellow: #d8e023;
    --leaf-sage: #c8e48e;
    --ink: #262626;
    --brand-ink: #f2f8d4;
    --rule: #5f8f3a;
  }
  html, body {
    margin: 0;
    padding: 0;
    overflow: hidden;
    background: #ffffff;
  }
  .card {
    position: relative;
    width: 1200px;
    height: 694px;
    background: var(--card-bg);
    overflow: hidden;
    font-family: "Didact Gothic", "Century Gothic", sans-serif;
    color: var(--ink);
  }
  .card__art {
    position: absolute;
    inset: 0;
    width: 1200px;
    height: 694px;
  }
  .brand {
    position: absolute;
    top: 100px;
    right: 150px;
    font-size: 24px;
    line-height: 1;
    color: var(--brand-ink);
    white-space: nowrap;
  }
  .brand-mark {
    position: absolute;
    top: 26px;
    right: 22px;
    width: 108px;
    height: 108px;
    background: var(--leaf-yellow);
  }
  .person {
    position: absolute;
    left: 620px;
    top: 290px;
    width: 492px;
    text-align: center;
  }
  .person__name {
    margin: 0;
    font-size: 60px;
    font-weight: 400;
    letter-spacing: 1px;
    line-height: 1;
  }
  .person__title {
    display: inline-block;
    margin: 14px 0 0;
    font-size: 42px;
    line-height: 1.1;
    padding: 0 14px 10px;
    border-bottom: 3px solid var(--rule);
  }
  .contact {
    position: absolute;
    left: 94px;
    top: 564px;
    margin: 0;
    font-size: 28px;
    line-height: 38px;
  }
  .contact__label {
    display: inline-block;
    margin-right: 8px;
  }
  .contact__label--short { min-width: 100px; margin-right: 0; }
  .location {
    position: absolute;
    right: 30px;
    top: 602px;
    margin: 0;
    font-size: 28px;
    line-height: 38px;
    text-align: right;
    font-style: normal;
  }
</style>
</head>
<body>
<main class="card">
  <svg class="card__art" viewBox="0 0 1060 614" preserveAspectRatio="none" role="img" aria-label="Sweeping green and yellow leaf-blade artwork across the top left corner">
    <defs>
      <linearGradient id="leafSweep" x1="0" y1="1" x2="1" y2="0">
        <stop offset="0" stop-color="var(--leaf-dark)"/>
        <stop offset="0.45" stop-color="var(--leaf-mid)"/>
        <stop offset="0.75" stop-color="var(--leaf-dark)"/>
        <stop offset="1" stop-color="var(--leaf-yellow)"/>
      </linearGradient>
    </defs>
    <path fill="var(--leaf-sage)" d="M380,230 C600,170 820,150 1060,140 V165 C820,172 600,195 410,240 Z"/>
    <path fill="url(#leafSweep)"
          d="M0,0 H1060 V145 C820,150 600,175 390,228 C240,320 100,460 15,605 H0 Z"/>
  </svg>

  <div class="brand">Marsh and Partners</div>
  <div class="brand-mark"></div>

  <section class="person">
    <h1 class="person__name">Daniel Hartley</h1>
    <p class="person__title">President</p>
  </section>

  <p class="contact">
    <span class="contact__label contact__label--short">Cell:</span>(555) 410-0127<br>
    <span class="contact__label">Office:</span>(555) 422-0150<br>
    <span class="contact__label">E-mail:</span>daniel.h@mp-demo.com
  </p>

  <address class="location">
    www.marshandpartners-demo.net<br>
    4120 North Elm Austin, TX 78700
  </address>
</main>
</body>
</html>
```